Tomas's Business Cards

My husband is a self employed Cabinet Maker... who contracts to Building companies and clients directly.
He installs kitchesn, designs and also completes renovations and building work.

I would like a small, FUNKY, simple but eye catching design.

It needs to incorporate the following.
Custom Cabinets / Installations / Renovations / Design

Commercial and Residential

He does not have a Website or Chatterly,
contact number is 0438 207 619 and email is tomasvelkin@quillmail.example

I would like a Grey/Silver on black, or blue covering.. I am open to colour designs?

Thank you. :-)

Target Market(s)

Building Companies
Clients
Other Trades people onsite,. to give out at job sites

Industry/Entity Type

Business

Contact Information for Business Card

Phone: 0438 207 619
Email: tomasvelkin@quillmail.example

Font styles to use
Sans Serif

Colors
0592cd
747474
474747
1b1b1b
85cae6

Requirements
Must have
• Funky, simple, eye catching design
• Would like use of Silver/Grey - and a colour that would complement this.
• Am open to ideas :-)
Nice to have
• We do not have a logo or picture, will leave this up to you if you think an image would be beneficial???
• Thank you.

```html
<!DOCTYPE html>
<html lang="en">
<head>
<meta charset="utf-8">
<title>Tomas Velkin – Business Card</title>
<link rel="stylesheet" href="https://fonts.googleapis.com/css2?family=Questrial&display=swap">
<style>
  :root {
    --backdrop: #1b1b1b;
    --silver-light: #e4e4e4;
    --silver: #c4c4c4;
    --silver-dark: #a3a3a3;
    --grey: #747474;
    --ink: #1b1b1b;
    --ink-soft: #474747;
    --blue: #0592cd;
    --blue-light: #85cae6;
    --card-shadow: rgba(0, 0, 0, 0.6);
  }

  * { margin: 0; padding: 0; box-sizing: border-box; }

  html, body {
    width: 1200px;
    height: 900px;
    overflow: hidden;
  }

  body {
    background: var(--backdrop);
    font-family: "Questrial", "Century Gothic", sans-serif;
    color: var(--ink);
    position: relative;
  }

  .business-card {
    position: absolute;
    left: 100px;
    top: 160px;
    width: 1000px;
    height: 580px;
    box-shadow: 0 18px 40px var(--card-shadow);
    overflow: hidden;
  }

  .card-surface {
    position: absolute;
    inset: 0;
    background: linear-gradient(100deg, var(--silver-light) 0%, var(--silver) 50%, var(--silver-dark) 100%);
  }

  .brand-mark {
    position: absolute;
    left: 50px;
    top: 222px;
    width: 150px;
    height: 150px;
    border-radius: 50%;
    background: var(--blue);
  }

  .owner-name {
    position: absolute;
    left: 222px;
    top: 210px;
    font-size: 64px;
    font-weight: 400;
    line-height: 1.0;
    letter-spacing: 0.5px;
    color: var(--ink);
  }

  .divider {
    position: absolute;
    left: 560px;
    top: 160px;
    width: 3px;
    height: 150px;
    background: var(--blue);
  }

  .contact {
    position: absolute;
    right: 44px;
    top: 162px;
    list-style: none;
    text-align: right;
    color: var(--ink-soft);
  }

  .contact-phone {
    font-size: 38px;
    letter-spacing: 2px;
    line-height: 1.2;
  }

  .contact-email {
    font-size: 26px;
    letter-spacing: 0.5px;
    margin-top: 8px;
  }

  .services {
    position: absolute;
    left: 50px;
    top: 398px;
    font-size: 33px;
    letter-spacing: 1px;
    white-space: nowrap;
    color: var(--ink);
  }

  .sectors {
    position: absolute;
    left: 340px;
    top: 448px;
    font-size: 33px;
    letter-spacing: 1px;
    white-space: nowrap;
    color: var(--ink);
  }
</style>
</head>
<body>
  <article class="business-card">
    <div class="card-surface" aria-hidden="true"></div>

    <div class="brand-mark" aria-hidden="true"></div>
    <h1 class="owner-name">Tomas<br>Velkin</h1>

    <div class="divider" aria-hidden="true"></div>
    <ul class="contact">
      <li class="contact-phone">0438 207 619</li>
      <li class="contact-email">tomasvelkin@quillmail.example</li>
    </ul>

    <p class="services">Custom Cabinets / Installations / Renovations / Design</p>
    <p class="sectors">Commercial and Residential</p>
  </article>
</body>
</html>
```